Business Card - connecting 2 souls and beggining the journey of self discovery

Logo on the front
with tag line

On the back list of services and contact details

Seminars
workshops
Coaching
podcasts

Daniel Porthwick
Health & Wellbeing Life Coach
0491 372 815
daniel@wovenpathwellness.example
wovenpathwellness.example

Industry/Entity Type

Life Coaching

Contact Information for Business Card

I like the use of colour from the logo to be used. I'm not a fan of white.

Requirements
Must have
• My tagline: Every good path begins within you
Nice to have
• Use of colour that is in the mind body soul logo

```html
<!DOCTYPE html>
<html lang="en">
<head>
<meta charset="utf-8">
<title>Woven Path Wellness — Business Card</title>
<link rel="stylesheet" href="https://fonts.googleapis.com/css2?family=Montserrat:wght@400;500;600;700;800&display=swap">
<style>
  :root {
    --backdrop: #2b2b2d;
    --coral: #ee6a6e;
    --coral-soft: #f07a6a;
    --amber: #f6a93c;
    --sun: #f7c42a;
    --ember: #e9512f;
    --ember-deep: #e4452c;
    --cream: #fffaf2;
    --ink: #2a2a2a;
    --card-w: 900px;
    --card-h: 514px;
  }
  * { box-sizing: border-box; margin: 0; padding: 0; }
  html, body {
    width: 1200px; height: 1200px; overflow: hidden;
    background: var(--backdrop);
    font-family: "Montserrat", sans-serif;
  }
  .sheet {
    width: 1200px; height: 1200px;
    display: flex; flex-direction: column; align-items: center; justify-content: center;
    gap: 56px;
  }
  .card {
    position: relative;
    width: var(--card-w); height: var(--card-h);
    border-radius: 4px;
    overflow: hidden;
    box-shadow: 0 14px 34px rgba(0,0,0,.45);
  }

  /* ---------- Front ---------- */
  .card--front {
    background: radial-gradient(ellipse 60% 62% at 50% 52%, var(--amber) 0%, var(--coral-soft) 58%, var(--coral) 100%);
    display: flex; flex-direction: column; align-items: center;
  }
  .brand-mark {
    margin-top: 78px;
    width: 170px; height: 170px;
    border-radius: 50%;
    background: var(--sun);
  }
  .brand-name {
    margin-top: 40px;
    color: var(--cream);
    font-weight: 800;
    font-size: 46px;
    letter-spacing: .5px;
    text-transform: uppercase;
  }
  .tagline {
    margin-top: 14px;
    display: flex; align-items: center; gap: 18px;
    color: var(--sun);
    font-weight: 600;
    font-size: 21px;
    letter-spacing: .6px;
  }
  .tagline::before, .tagline::after {
    content: ""; width: 74px; height: 2px; background: var(--sun);
  }

  /* ---------- Back ---------- */
  .card--back {
    background: radial-gradient(ellipse 48% 62% at 42% 30%, var(--sun) 0%, var(--amber) 32%, var(--coral-soft) 78%, var(--coral) 100%);
  }
  .service-band {
    position: absolute; inset: 0;
    background: linear-gradient(160deg, var(--ember) 0%, var(--ember-deep) 100%);
    clip-path: polygon(82% 0, 100% 0, 100% 100%, 49% 100%);
  }
  .service-band-edge {
    position: absolute; inset: 0;
    background: rgba(255,220,160,.35);
    clip-path: polygon(80.6% 0, 81.3% 0, 48.2% 100%, 47.5% 100%);
  }
  .identity {
    position: absolute; left: 64px; top: 92px;
    color: var(--cream);
  }
  .identity__name { font-weight: 500; font-size: 40px; letter-spacing: .4px; }
  .identity__role { font-weight: 500; font-size: 17px; margin-top: 2px; letter-spacing: .3px; }

  .contact-list {
    position: absolute; left: 64px; top: 240px;
    list-style: none;
    display: flex; flex-direction: column; gap: 24px;
    color: var(--cream);
    font-size: 19px; font-weight: 500; letter-spacing: .3px;
  }
  .contact-list li { display: flex; align-items: center; gap: 16px; }
  .contact-icon { width: 22px; height: 22px; flex: none; }

  .services {
    position: absolute; right: 70px; top: 190px;
    width: 190px;
    color: var(--cream);
  }
  .services__title {
    font-weight: 600; font-size: 26px; letter-spacing: 2px;
    padding-bottom: 10px;
    border-bottom: 2px solid var(--cream);
    margin-bottom: 18px;
    text-align: center;
  }
  .services__list { list-style: none; display: flex; flex-direction: column; gap: 14px; }
  .services__list li { display: flex; align-items: center; gap: 14px; font-size: 20px; font-weight: 500; }
  .tick-box { width: 28px; height: 26px; flex: none; }
</style>
</head>
<body>
<main class="sheet">

  <section class="card card--front" aria-label="Business card front">
    <div class="brand-mark" aria-hidden="true"></div>
    <h1 class="brand-name">Woven Path Wellness</h1>
    <p class="tagline">Every good path begins within you</p>
  </section>

  <section class="card card--back" aria-label="Business card back">
    <div class="service-band"></div>
    <div class="service-band-edge"></div>

    <div class="identity">
      <h2 class="identity__name">Daniel Porthwick</h2>
      <p class="identity__role">Health &amp; Wellbeing Life Coach</p>
    </div>

    <ul class="contact-list">
      <li>
        <svg class="contact-icon" viewBox="0 0 24 24" aria-hidden="true">
          <circle cx="12" cy="12" r="12" fill="#f7c42a"/>
          <path d="M8.2 6.5l2 2.2-1 1.5c.8 1.6 2 2.8 3.6 3.6l1.5-1 2.2 2-1 1.8c-4.3-.4-8.3-4.4-8.7-8.7z" fill="#fffaf2"/>
        </svg>
        <span>0491 372 815</span>
      </li>
      <li>
        <svg class="contact-icon" viewBox="0 0 24 24" aria-hidden="true">
          <circle cx="12" cy="12" r="12" fill="#f7c42a"/>
          <circle cx="12" cy="12" r="4.5" fill="none" stroke="#fffaf2" stroke-width="2"/>
        </svg>
        <span>daniel@wovenpathwellness.example</span>
      </li>
      <li>
        <svg class="contact-icon" viewBox="0 0 24 24" aria-hidden="true">
          <circle cx="12" cy="12" r="12" fill="#f7c42a"/>
          <rect x="6" y="7.5" width="12" height="9" rx="1.5" fill="#fffaf2"/>
          <rect x="6" y="7.5" width="12" height="2.4" fill="#f6a93c"/>
        </svg>
        <span>wovenpathwellness.example</span>
      </li>
    </ul>

    <div class="services">
      <h3 class="services__title">Services</h3>
      <ul class="services__list">
        <li><svg class="tick-box" viewBox="0 0 28 26" aria-hidden="true"><rect x="1.5" y="7.5" width="16" height="16" fill="none" stroke="#2a2a2a" stroke-width="2"/><path d="M5 15l4.5 5L26 2" fill="none" stroke="#2a2a2a" stroke-width="2.6" stroke-linecap="round"/></svg>Seminars</li>
        <li><svg class="tick-box" viewBox="0 0 28 26" aria-hidden="true"><rect x="1.5" y="7.5" width="16" height="16" fill="none" stroke="#2a2a2a" stroke-width="2"/><path d="M5 15l4.5 5L26 2" fill="none" stroke="#2a2a2a" stroke-width="2.6" stroke-linecap="round"/></svg>Workshops</li>
        <li><svg class="tick-box" viewBox="0 0 28 26" aria-hidden="true"><rect x="1.5" y="7.5" width="16" height="16" fill="none" stroke="#2a2a2a" stroke-width="2"/><path d="M5 15l4.5 5L26 2" fill="none" stroke="#2a2a2a" stroke-width="2.6" stroke-linecap="round"/></svg>Coaching</li>
        <li><svg class="tick-box" viewBox="0 0 28 26" aria-hidden="true"><rect x="1.5" y="7.5" width="16" height="16" fill="none" stroke="#2a2a2a" stroke-width="2"/><path d="M5 15l4.5 5L26 2" fill="none" stroke="#2a2a2a" stroke-width="2.6" stroke-linecap="round"/></svg>Podcasts</li>
      </ul>
    </div>
  </section>

</main>
</body>
</html>
```